Staffing and Consulting Service Company needs Business Cards

We need to have business cards for our business. You can check our website www.quelbrantix.com to see the branding we are using. The logo is in the website.
We use a tag line Staffing & Consulting Solutions Made Easy.
We use different blues in the logo and we use the red for the Company name.
As you can see in the website there is a gradient in the bottom part of each page that includes some of the dots we use for the logo.
We will need the following fields on the design:
Company Name
Employee Name
Title
Address
Tel
Email
Website
Can be Single or Double Sided
There is no preference for single or double sided.
Target Market(s)
Companies in need of IT staffing and IT consulting services
Industry/Entity Type
Business
Look and feel

```html
<!DOCTYPE html>
<html lang="en">
<head>
<meta charset="utf-8">
<title>Quelbrantix Business Cards</title>
<link rel="stylesheet" href="https://fonts.googleapis.com/css2?family=Arimo:wght@400;700&display=swap">
<style>
  :root {
    --page-bg: #ecebef;
    --navy: #1f2160;
    --navy-deep: #15174a;
    --violet: #6a6db8;
    --lavender: #b9bbe4;
    --lavender-soft: #dcddf1;
    --maroon: #7a2a33;
    --ink: #1d1f55;
    --text-dark: #2a2a3a;
    --card-white: #ffffff;
    --dot-grey: #e4e4ea;
  }
  * { box-sizing: border-box; margin: 0; padding: 0; }
  html, body { width: 1200px; height: 784px; overflow: hidden; }
  body {
    background: var(--page-bg);
    font-family: "Arimo", Arial, sans-serif;
    position: relative;
  }
  .card {
    position: absolute;
    width: 540px;
    height: 309px;
    top: 238px;
    border-radius: 4px;
    overflow: hidden;
    box-shadow: 0 6px 18px rgba(20, 20, 50, 0.18);
  }
  /* Back side */
  .card-back {
    left: 30px;
    background: linear-gradient(120deg, var(--navy-deep) 0%, var(--navy) 45%, #4a4d9a 100%);
  }
  .card-back .dot-field {
    position: absolute;
    inset: 0;
    background: radial-gradient(ellipse at 85% 30%, rgba(170, 172, 230, 0.55) 0%, rgba(120, 122, 200, 0.25) 40%, rgba(0, 0, 0, 0) 75%);
  }
  .card-back .web-address {
    position: absolute;
    left: 60px;
    top: 150px;
    color: #ffffff;
    font-size: 19px;
    letter-spacing: 0.42em;
    transform: rotate(-12deg);
    transform-origin: left center;
    white-space: nowrap;
  }
  /* Front side */
  .card-front {
    left: 630px;
    background: var(--card-white);
  }
  .card-front .dot-field {
    position: absolute;
    right: 20px;
    top: 50px;
    width: 200px;
    height: 180px;
    background: radial-gradient(ellipse at center, var(--dot-grey) 0%, rgba(228, 228, 234, 0.6) 50%, rgba(255, 255, 255, 0) 75%);
  }
  .card-front .swoosh {
    position: absolute;
    inset: 0;
  }
  .brand {
    position: absolute;
    left: 36px;
    top: 38px;
    display: flex;
    align-items: center;
    gap: 14px;
  }
  .brand-square {
    width: 60px;
    height: 60px;
    background: var(--navy);
    border-radius: 5px;
  }
  .brand-name {
    color: var(--maroon);
    font-size: 40px;
    font-weight: 400;
    letter-spacing: 0.06em;
  }
  .person {
    position: absolute;
    left: 54px;
    top: 122px;
  }
  .person-name {
    color: var(--maroon);
    font-size: 19px;
    font-weight: 700;
  }
  .person-title {
    color: var(--text-dark);
    font-size: 12px;
    margin-top: 3px;
  }
  .contact-list {
    position: absolute;
    left: 54px;
    top: 166px;
    list-style: none;
    color: var(--ink);
    font-size: 16px;
    line-height: 21px;
  }
  .contact-list li {
    display: flex;
    align-items: flex-start;
    gap: 7px;
  }
  .contact-list svg {
    width: 15px;
    height: 15px;
    margin-top: 3px;
    flex: none;
  }
  .contact-list .address span { display: block; }
</style>
</head>
<body>

  <section class="card card-back" aria-label="Card back">
    <div class="dot-field" role="img" aria-label="Soft field of light blue dots fading across the card"></div>
    <p class="web-address">www.quelbrantix.com</p>
  </section>

  <section class="card card-front" aria-label="Card front">
    <div class="dot-field" role="img" aria-label="Faint grey dot decoration"></div>

    <svg class="swoosh" viewBox="0 0 540 309" aria-hidden="true">
      <defs>
        <linearGradient id="band-fill" x1="0" y1="0" x2="1" y2="0">
          <stop offset="0" stop-color="#c9cbec"/>
          <stop offset="1" stop-color="#8f92d0"/>
        </linearGradient>
      </defs>
      <path d="M0 284 C200 302 400 268 540 162 L540 309 L0 309 Z" fill="var(--lavender-soft)"/>
      <path d="M0 302 C200 318 400 292 540 196 L540 309 L0 309 Z" fill="#ffffff"/>
      <path d="M0 290 C200 310 400 276 540 172 L540 190 C400 290 200 318 0 303 Z" fill="url(#band-fill)"/>
      <path d="M0 282 C200 302 400 266 540 160" fill="none" stroke="var(--violet)" stroke-width="2"/>
      <path d="M200 309 C330 300 440 270 540 235 L540 244 C450 278 340 305 260 309 Z" fill="var(--lavender)"/>
    </svg>

    <div class="brand">
      <div class="brand-square" aria-hidden="true"></div>
      <span class="brand-name">QUELBRANTIX</span>
    </div>

    <div class="person">
      <p class="person-name">Marlo Venter</p>
      <p class="person-title">Manager</p>
    </div>

    <ul class="contact-list">
      <li>
        <svg viewBox="0 0 16 16" aria-hidden="true"><path fill="var(--maroon)" d="M3.2 1.5l2.3 2.6-1.3 1.8c.9 2 2.5 3.6 4.5 4.5l1.8-1.3 2.6 2.3-1.4 2.1C6.6 14.9 1.1 9.4.7 3.5z"/></svg>
        <span>(555) 014-2297</span>
      </li>
      <li>
        <svg viewBox="0 0 16 16" aria-hidden="true"><rect x="1" y="3.5" width="14" height="10" rx="1" fill="var(--maroon)"/><path d="M1.5 4.5L8 9.5l6.5-5" fill="none" stroke="#fff" stroke-width="1.3"/></svg>
        <span>marlo@quelbrantix.com</span>
      </li>
      <li class="address">
        <svg viewBox="0 0 16 16" aria-hidden="true"><path fill="var(--maroon)" d="M8 1.5L.8 8h2.2v6.5h3.8v-4h2.4v4H13V8h2.2z"/></svg>
        <div><span>4410 Harbor Crest Lane Dunmore,</span><span>FL 30000</span></div>
      </li>
    </ul>
  </section>

</body>
</html>
```